Beacon Lending and Capital. We provide MOSTLY residential home mortgages in Florida AND commercial loans for investment properties throughout the United states.
I would love to emulate so of the lender sites that are available on the internet but I would like to have the site as popular as possible for SEO purposes. Clients can already click the link to take them to the mortgage application where they can complete that and upload documents. If you could polish that up for me that would be great. I can also provide you with great detail on loan programs that are currently being offered. WE OFFER ALL MORTGAGE LENDING PRODUCTS. I would also like to add something in reference to the rate but I don't think it's legal to actually state or promise a rate for mortgage since they vary based on loan type, client and other criteria...

On the Beacon real estate site I would like to add a link or some way for clients to be able to put in credit card information to render services ...

Please let me know what you need from me

Thank you !!

Current link to site to improve and code

https://beaconlendingandcapital.example/

Industry/Entity Type

Residential and commmercial lending

Coding

Coded - Design and coding required

Number of Pages Required

2 page

Requirements
Must have
• Love to integrate Mortgage interest rates even if general
Nice to have
• Link to fill out mortgage application via Quillo MLO software

```html
<!DOCTYPE html>
<html lang="en">
<head>
<meta charset="utf-8">
<title>Beacon Lending and Capital — Home Loans in Florida</title>
<link href="https://fonts.googleapis.com/css2?family=Poppins:wght@300;400;500;600;700&family=Montserrat:wght@400;500;600;700&display=swap" rel="stylesheet">
<style>
:root{
  --lime:#8cb83f;
  --lime-dark:#76a02c;
  --lime-soft:#f6fae8;
  --lime-wash:#e9f1d2;
  --ink:#1d3a1c;
  --text:#555b55;
  --navy:#0b2647;
  --white:#ffffff;
}
*{box-sizing:border-box;margin:0;padding:0}
html,body{width:1200px;height:5074px;overflow:hidden}
body{font-family:"Montserrat",sans-serif;color:var(--text);background:var(--white)}
.page{position:relative;width:1200px;height:5074px;overflow:hidden}
.abs{position:absolute}
a{color:inherit;text-decoration:none}
h1,h2,h3{font-family:"Poppins",sans-serif;color:var(--ink)}
.eyebrow{font-size:12px;letter-spacing:.5px;color:var(--lime);text-transform:uppercase;text-align:center}
.section-title{font-size:30px;font-weight:700;text-align:center}
.btn{display:inline-flex;align-items:center;justify-content:center;font-family:"Poppins",sans-serif;font-weight:600;font-size:12px;letter-spacing:.3px;text-transform:uppercase;height:42px;padding:0 26px;border-radius:0 22px 0 22px;background:var(--lime);color:#fff}
.btn-outline{background:transparent;color:var(--ink);border:2px solid var(--ink)}

/* top bar */
.topbar{top:20px;left:90px;right:90px;height:20px;font-size:11px;color:var(--ink);display:flex;align-items:center}
.topbar .item{display:flex;align-items:center;gap:8px;margin-right:40px}
.topbar .links{margin-left:auto;display:flex;gap:30px}
.topbar .links a{text-decoration:underline;font-weight:500;text-transform:uppercase}

/* header */
.hero{top:0;left:0;width:1200px;height:770px;background:linear-gradient(90deg,#f2f7e3 0%,#eef5da 35%,#d8e6b6 60%,#c7d7a2 100%)}
.hero-photo{top:140px;left:430px;width:770px;height:630px;background:radial-gradient(ellipse at 55% 40%,#e7d4bd 0%,#c9c3a2 35%,#b7c78f 70%,#dce8bf 100%);opacity:.9}
.hero-fade{top:140px;left:0;width:800px;height:630px;background:linear-gradient(90deg,#f2f7e3 0%,#f2f7e3 50%,rgba(242,247,227,0) 100%)}
.header{top:50px;left:50px;width:1110px;height:90px;background:#fff;border-radius:0 40px 0 40px;display:flex;align-items:center;padding:0 40px 0 30px}
.brand{display:flex;align-items:center;gap:10px}
.brand-mark{width:56px;height:56px;border-radius:50%;background:var(--ink)}
.brand-name{font-family:"Montserrat",sans-serif;font-size:12px;font-weight:600;color:var(--lime);letter-spacing:.5px;text-transform:uppercase;line-height:1.3;width:200px}
.nav{display:flex;gap:40px;margin-left:50px;font-size:12px;font-weight:500;color:var(--ink);text-transform:uppercase}
.header .btn{margin-left:auto;height:36px;font-size:11px;padding:0 26px}
.hero-copy{top:252px;left:85px;width:500px}
.hero-copy h1{font-size:36px;line-height:1.2;font-weight:700}
.hero-copy p{margin-top:38px;font-size:11px;color:var(--ink);text-transform:uppercase;line-height:1.4;width:360px}
.hero-actions{margin-top:30px;display:flex;gap:30px}
.hero-wave{top:600px;left:0}

/* about */
.about-block{top:851px;left:292px;width:286px;height:120px;background:var(--lime)}
.about-photo{top:872px;left:79px;width:477px;height:425px;background:linear-gradient(135deg,#c8a27c 0%,#e2cdb3 40%,#b38d6a 100%);border-radius:0 0 80px 0}
.about-copy{top:930px;left:628px;width:520px}
.about-copy .eyebrow{text-align:left}
.about-copy h2{font-size:30px;font-weight:700;margin-top:8px}
.about-copy p{font-size:14px;line-height:1.45;margin-top:22px;color:#5f645f}
.about-copy p + p{margin-top:18px}
.about-copy .btn{margin-top:30px}

/* process */
.process{top:1400px;left:0;width:1200px}
.process .section-title{margin-top:8px;font-size:28px}
.steps{position:absolute;top:1585px;left:80px;width:1040px;display:flex;justify-content:space-between}
.step{width:220px;text-align:center}
.step-num{font-family:"Poppins",sans-serif;font-weight:300;font-size:88px;line-height:1;color:transparent;-webkit-text-stroke:1.6px var(--ink)}
.step-label{margin-top:14px;font-family:"Poppins",sans-serif;font-size:17px;font-weight:600;color:var(--ink);line-height:1.35}
.step-dots{position:absolute;top:1628px;height:0;border-top:2px dotted var(--lime)}

/* loans */
.loans-bg{top:1930px;left:0}
.loans-head{top:2100px;left:0;width:1200px}
.loan-card{width:282px;height:282px;background:#fff;border-radius:0 40px 0 40px;box-shadow:0 6px 22px rgba(60,80,30,.07);text-align:center;padding:30px 28px 0}
.loan-icon{width:100px;height:100px;border-radius:50%;background:var(--lime);margin:0 auto;display:flex;align-items:center;justify-content:center}
.loan-card h3{margin-top:16px;font-size:19px;font-weight:600;line-height:1.2}
.loan-card p{margin-top:16px;font-size:13px;line-height:1.35;color:#6b706b}

/* properties */
.props-head{top:3135px;left:0;width:1200px}
.props-head .section-title{margin-top:10px}
.prop{width:228px;height:410px;background:#fff;box-shadow:0 6px 22px rgba(0,0,0,.08)}
.prop-img{position:relative;height:154px;background:linear-gradient(180deg,#6c7ea3 0%,#8b8f93 55%,#58614a 100%)}
.prop-img .tag{position:absolute;left:18px;bottom:30px;font-size:11px;color:var(--lime)}
.prop-img .price{position:absolute;left:18px;bottom:8px;font-family:"Poppins",sans-serif;font-size:15px;font-weight:600;color:#fff}
.prop-body{padding:14px 18px}
.prop-body h3{font-size:15px;font-weight:600}
.prop-body .addr{font-size:10px;margin-top:2px}
.prop-body .desc{font-size:10.5px;margin-top:18px;line-height:1.45;color:#6b706b}
.meta{display:flex;flex-wrap:wrap;gap:4px 12px;margin-top:16px;font-size:9px;color:#444}
.meta span::before{content:"";display:inline-block;width:8px;height:6px;background:var(--ink);margin-right:4px;border-radius:1px}
.prop .apply{display:block;margin:14px 18px 0;height:28px;line-height:28px;text-align:center;background:var(--lime);color:#fff;font-size:11px;font-weight:600}

/* faq */
.faq{top:3990px;left:75px;width:512px}
.faq .eyebrow{text-align:left}
.faq h2{font-size:29px;font-weight:600;margin-top:4px}
.faq-item{background:#fff;box-shadow:0 4px 18px rgba(0,0,0,.06);display:flex;gap:20px;padding:14px 20px}
.faq-toggle{flex:none;width:30px;height:30px;display:flex;align-items:center;justify-content:center;color:#fff;font-size:22px;font-weight:600;line-height:1}
.faq-q{font-family:"Poppins",sans-serif;font-size:16px;font-weight:600;color:var(--ink);padding-top:4px}
.faq-a{font-size:11px;margin-top:8px;line-height:1.35;color:#6b706b}
.faq-block{top:3946px;left:852px;width:268px;height:162px;background:var(--lime)}
.faq-photo{top:3970px;left:650px;width:452px;height:394px;background:linear-gradient(135deg,#c9b59a 0%,#e9dccb 45%,#a98d70 100%);border-radius:60px 0 60px 0}

/* footer */
.footer-bg{top:4500px;left:0}
.footer-brand{top:4696px;left:75px;width:260px}
.footer-brand .brand-mark{width:52px;height:52px;background:#fff}
.footer-brand .brand-name{color:var(--lime);font-size:10px;width:190px}
.footer-call{margin-top:36px;font-family:"Poppins",sans-serif;font-size:17px;font-weight:600;color:var(--lime)}
.footer-phone{margin-top:10px;font-size:13px;color:#fff;display:flex;gap:10px;align-items:center}
.socials{display:flex;gap:14px;margin-top:28px}
.socials span{width:16px;height:16px;border-radius:50%;background:var(--lime)}
.footer-rule{top:4895px;left:315px;width:1px;height:80px;background:#2d4a6e}
.fcol{top:4692px;width:180px;color:#fff;font-size:11px}
.fcol h4{display:inline-block;background:var(--lime);color:#fff;font-size:10px;font-weight:500;padding:2px 8px;margin-bottom:10px}
.fcol li{list-style:none;line-height:1.25;margin-bottom:12px}
.fcol h4.inline{margin-top:2px}
.legal{top:5040px;left:0;width:1200px;height:34px;background:var(--lime);color:#fff;font-size:10px;display:flex;align-items:center;justify-content:space-between;padding:0 75px}
</style>
</head>
<body>
<div class="page">

  <!-- Hero -->
  <section class="abs hero" aria-label="Hero"></section>
  <div class="abs hero-photo" role="img" aria-label="Photo of a smiling couple reviewing their mortgage on a laptop at home"></div>
  <div class="abs hero-fade"></div>

  <div class="abs topbar">
    <div class="item">
      <svg width="12" height="12" viewBox="0 0 24 24"><path fill="#1d3a1c" d="M6.6 10.8a15 15 0 0 0 6.6 6.6l2.2-2.2c.3-.3.7-.4 1-.2 1.1.4 2.3.6 3.6.6.6 0 1 .4 1 1V20c0 .6-.4 1-1 1A17 17 0 0 1 3 4c0-.6.4-1 1-1h3.5c.6 0 1 .4 1 1 0 1.3.2 2.5.6 3.6.1.3 0 .7-.2 1z"/></svg>
      <span>888 888 8888</span>
    </div>
    <div class="item">
      <svg width="13" height="10" viewBox="0 0 24 18"><rect x="1" y="1" width="22" height="16" rx="2" fill="#1d3a1c"/><path d="M2 2l10 8 10-8" stroke="#fff" stroke-width="2" fill="none"/></svg>
      <span>info@beaconlending.example</span>
    </div>
    <div class="links"><a href="#">Mortgage Calculator</a><a href="#">See Rates Now</a></div>
  </div>

  <header class="abs header">
    <div class="brand"><span class="brand-mark"></span><span class="brand-name">Beacon Lending and Capital</span></div>
    <nav class="nav"><a href="#">Home</a><a href="#">About</a><a href="#">Services</a><a href="#">Team</a><a href="#">Testimonials</a><a href="#">Contact</a></nav>
    <a class="btn" href="#">Apply Now</a>
  </header>

  <div class="abs hero-copy">
    <h1>Your Best Resources for Hassle-Free, Low Cost Mortgage Origination</h1>
    <p>Residential home loans in Florida and commercial lending in America</p>
    <div class="hero-actions">
      <a class="btn" href="#">Get a Free Quote</a>
      <a class="btn btn-outline" href="#">Mortgage Application</a>
    </div>
  </div>

  <svg class="abs hero-wave" width="1200" height="180" viewBox="0 0 1200 180" aria-hidden="true">
    <path d="M0 40 C 160 110, 320 120, 500 80 C 720 30, 880 20, 1040 90 C 1110 120, 1170 140, 1200 150 L1200 180 L0 180 Z" fill="#fff"/>
  </svg>

  <!-- About -->
  <div class="abs about-block"></div>
  <div class="abs about-photo" role="img" aria-label="Photo of a couple meeting with a loan advisor at a desk"></div>
  <section class="abs about-copy">
    <div class="eyebrow">Who We Are</div>
    <h2>About Us</h2>
    <p>Morbi eget maximus habitasse id malesuada mi hendrerit. Magnis volutpat mi consectetur etiam suspendisse pellentesque nostra odio. Ridiculus inceptos eleifend dolor porttitor orci natoque penatibus.</p>
    <p>Magna non dolor facilisis sodales proin. Lobortis sagittis imperdiet litora laoreet erat vivamus habitasse at malesuada.</p>
    <a class="btn" href="#">More About Us</a>
  </section>

  <!-- Process -->
  <section class="abs process">
    <div class="eyebrow">How Do We Do It?</div>
    <h2 class="section-title">Find The Right Home Loan For You</h2>
  </section>
  <div class="abs step-dots" style="left:255px;width:130px"></div>
  <div class="abs step-dots" style="left:528px;width:130px"></div>
  <div class="abs step-dots" style="left:800px;width:130px"></div>
  <div class="steps">
    <div class="step"><div class="step-num">01</div><div class="step-label">Pre-Qualification<br>and Documentation</div></div>
    <div class="step"><div class="step-num">02</div><div class="step-label">Begin the Loan<br>Process</div></div>
    <div class="step"><div class="step-num">03</div><div class="step-label">Inspection and<br>Appraisal</div></div>
    <div class="step"><div class="step-num">04</div><div class="step-label">Final Approval and<br>Closing</div></div>
  </div>
  <a class="abs btn" href="#" style="top:1779px;left:512px;width:185px">Get a Free Quote</a>

  <!-- Loans -->
  <svg class="abs loans-bg" width="1200" height="1090" viewBox="0 0 1200 1090" aria-hidden="true">
    <path d="M0 20 C 200 90, 420 110, 640 70 C 860 30, 1050 0, 1200 50 L1200 1060 C 1000 1000, 780 1000, 560 1040 C 340 1080, 160 1070, 0 1030 Z" fill="#f6fae8"/>
  </svg>
  <section class="abs loans-head">
    <div class="eyebrow">What We Do</div>
    <h2 class="section-title" style="margin-top:8px">Loans We Offer</h2>
  </section>

  <article class="abs loan-card" style="top:2220px;left:85px">
    <div class="loan-icon"><svg width="50" height="50" viewBox="0 0 50 50" fill="none" stroke="#fff" stroke-width="2.5"><circle cx="25" cy="20" r="10"/><path d="M21 20h8M25 16v8M6 38h10l10 4 18-8"/></svg></div>
    <h3>Conventional<br>Loans</h3>
    <p>Vitae lorem risus venenatis facilisis mattis curabitur porttitor platea.</p>
  </article>
  <article class="abs loan-card" style="top:2212px;left:441px">
    <div class="loan-icon"><svg width="50" height="50" viewBox="0 0 50 50" fill="none" stroke="#fff" stroke-width="2.5"><path d="M12 24l13-11 13 11v12H12z"/><path d="M6 40h10l10 4 18-8"/></svg></div>
    <h3>SHA<br>Loans</h3>
    <p>Vitae lorem risus venenatis facilisis mattis curabitur porttitor platea.</p>
  </article>
  <article class="abs loan-card" style="top:2205px;left:798px">
    <div class="loan-icon"><svg width="50" height="50" viewBox="0 0 50 50" fill="none" stroke="#fff" stroke-width="2.5"><rect x="13" y="8" width="24" height="32" rx="2"/><path d="M18 18h14M18 25h14M18 32h8"/></svg></div>
    <h3>Refinance<br>Loans</h3>
    <p>Vitae lorem risus venenatis facilisis mattis curabitur porttitor platea.</p>
  </article>
  <article class="abs loan-card" style="top:2545px;left:80px">
    <div class="loan-icon"><svg width="50" height="50" viewBox="0 0 50 50" fill="none" stroke="#fff" stroke-width="2.5"><rect x="10" y="10" width="26" height="32" rx="2"/><path d="M16 20h14M16 27h14M16 34h8"/><path d="M32 30l8-8"/></svg></div>
    <h3>Home<br>Loans</h3>
    <p>Vitae lorem risus venenatis facilisis mattis curabitur porttitor platea.</p>
  </article>
  <article class="abs loan-card" style="top:2538px;left:436px">
    <div class="loan-icon"><svg width="50" height="50" viewBox="0 0 50 50" fill="none" stroke="#fff" stroke-width="2.5"><circle cx="25" cy="25" r="18"/><path d="M16 26l9-8 9 8v9H16z"/></svg></div>
    <h3>Renovation &amp;<br>Construction</h3>
    <p>Vitae lorem risus venenatis facilisis mattis curabitur porttitor platea.</p>
  </article>
  <article class="abs loan-card" style="top:2530px;left:793px">
    <div class="loan-icon"><svg width="50" height="50" viewBox="0 0 50 50" fill="none" stroke="#fff" stroke-width="2.5"><rect x="13" y="8" width="24" height="32" rx="2"/><circle cx="24" cy="22" r="6"/><path d="M28 26l6 6"/></svg></div>
    <h3>Rerverse<br>Mortgage</h3>
    <p>Vitae lorem risus venenatis facilisis mattis curabitur porttitor platea.</p>
  </article>

  <!-- Properties -->
  <section class="abs props-head">
    <div class="eyebrow">Properties Available</div>
    <h2 class="section-title">Empowering Your Homeownership Journey</h2>
  </section>

  <article class="abs prop" style="top:3294px;left:112px">
    <div class="prop-img" role="img" aria-label="Photo of suburban family houses"><span class="tag">House</span><span class="price">$110,000-$199,000</span></div>
    <div class="prop-body"><h3>Balaraja Garden City</h3><div class="addr">12 Sunset Street</div>
      <p class="desc">Primis aliquam praesent pulvinar metus mus magnis placerat vehicula enim.</p>
      <div class="meta"><span>2 Beds</span><span>2 Bath</span><span>1 Parking lot</span><span>1250sqft</span></div></div>
    <a class="apply" href="#">Apply Now</a>
  </article>
  <article class="abs prop" style="top:3294px;left:355px">
    <div class="prop-img" role="img" aria-label="Photo of a modern apartment block" style="background:linear-gradient(180deg,#4d5258 0%,#6e6a66 60%,#3e4240 100%)"><span class="tag">Apartment</span><span class="price">$50,000-$99,000</span></div>
    <div class="prop-body"><h3>Ophelia Apartment</h3><div class="addr">34 Union Avenue</div>
      <p class="desc">Primis aliquam praesent pulvinar metus mus magnis placerat vehicula enim.</p>
      <div class="meta"><span>2 Beds</span><span>2 Bath</span><span>1 Parking lot</span><span>1250sqft</span></div></div>
    <a class="apply" href="#">Apply Now</a>
  </article>
  <article class="abs prop" style="top:3294px;left:595px">
    <div class="prop-img" role="img" aria-label="Photo of a large home at dusk" style="background:linear-gradient(180deg,#4a5a85 0%,#6d6f8c 55%,#3e4a3a 100%)"><span class="tag">Office &amp; Apartment</span><span class="price">$80,000-$150,000</span></div>
    <div class="prop-body"><h3>Twin Tower Office</h3><div class="addr">56 Washington Street</div>
      <p class="desc">Primis aliquam praesent pulvinar metus mus magnis placerat vehicula enim.</p>
      <div class="meta"><span>2 Beds</span><span>2 Bath</span><span>1 Parking lot</span><span>1250sqft</span></div></div>
    <a class="apply" href="#">Apply Now</a>
  </article>
  <article class="abs prop" style="top:3294px;left:837px">
    <div class="prop-img" role="img" aria-label="Photo of a modern timber-clad house" style="background:linear-gradient(180deg,#7d8a9a 0%,#7a5f4a 60%,#4b4a3e 100%)"><span class="tag">House</span><span class="price">$140,000-$220,000</span></div>
    <div class="prop-body"><h3>Serpong Smart Town</h3><div class="addr">78 Oak Boulevard</div>
      <p class="desc">Primis aliquam praesent pulvinar metus mus magnis placerat vehicula enim.</p>
      <div class="meta"><span>2 Beds</span><span>2 Bath</span><span>1 Parking lot</span><span>1250sqft</span></div></div>
    <a class="apply" href="#">Apply Now</a>
  </article>

  <a class="abs btn" href="#" style="top:3773px;left:486px;width:185px">View Properties</a>

  <!-- FAQ -->
  <section class="abs faq">
    <div class="eyebrow">FAQs</div>
    <h2>Frequently Asked Question</h2>
  </section>
  <div class="abs faq-item" style="top:4088px;left:75px;width:512px;height:110px">
    <span class="faq-toggle" style="background:var(--ink)">–</span>
    <div><div class="faq-q">What types of loans are available?</div>
      <div class="faq-a">Common types include personal loans, home loans mortgages, auto loans, student loans, and business loans.</div></div>
  </div>
  <div class="abs faq-item" style="top:4212px;left:75px;width:512px;height:54px">
    <span class="faq-toggle" style="background:var(--lime)">+</span>
    <div class="faq-q">How does the loan application process work?</div>
  </div>
  <div class="abs faq-item" style="top:4290px;left:75px;width:512px;height:60px">
    <span class="faq-toggle" style="background:var(--lime)">+</span>
    <div class="faq-q">What is the interest rate on a loan?</div>
  </div>
  <div class="abs faq-block"></div>
  <div class="abs faq-photo" role="img" aria-label="Photo of a couple on a sofa looking at a tablet beside moving boxes"></div>

  <!-- Footer -->
  <svg class="abs footer-bg" width="1200" height="574" viewBox="0 0 1200 574" aria-hidden="true">
    <path d="M0 30 C 200 -10, 420 40, 640 60 C 860 80, 1050 40, 1200 10 L1200 574 L0 574 Z" fill="#0b2647"/>
  </svg>
  <div class="abs footer-brand">
    <div class="brand"><span class="brand-mark"></span><span class="brand-name">Beacon Lending and Capital</span></div>
    <div class="footer-call">Call Us Tod at</div>
    <div class="footer-phone"><svg width="12" height="12" viewBox="0 0 24 24"><path fill="#fff" d="M6.6 10.8a15 15 0 0 0 6.6 6.6l2.2-2.2c.3-.3.7-.4 1-.2 1.1.4 2.3.6 3.6.6.6 0 1 .4 1 1V20c0 .6-.4 1-1 1A17 17 0 0 1 3 4c0-.6.4-1 1-1h3.5c.6 0 1 .4 1 1 0 1.3.2 2.5.6 3.6.1.3 0 .7-.2 1z"/></svg>888 888 8888</div>
    <div class="socials"><span></span><span></span><span></span></div>
  </div>
  <div class="abs footer-rule"></div>

  <div class="abs fcol" style="left:376px">
    <h4>Loan Programs</h4>
    <ul><li>Conventional Loans</li><li>USDA Home Loans</li><li>FHA Loans</li><li>VA (Veterans Affairs) Loans</li><li>Reverse Mortgage</li><li>Jumbo Loans</li><li>Renovation Loans</li><li>Bank Statement Programs</li><li>Construction Loans</li><li>Investment Property<br>Programs</li></ul>
  </div>
  <div class="abs fcol" style="left:581px">
    <h4>Our Company</h4>
    <ul><li>Culture</li><li>Employee Owned</li><li>Customer Reviews</li><li>News &amp; Media</li><li>Legal &amp; Regulatory</li><li>Accessibility Statement</li><li>Terms &amp; Conditions</li><li>SMS Opt Out</li></ul>
  </div>
  <div class="abs fcol" style="left:786px">
    <h4>Resources</h4>
    <ul><li>Learning Center</li><li>Frequently Asked<br>Questions</li><li>Mortgage Calculators</li><li>Ultimate Home Buyers<br>Guide</li><li>Ultimate Guide to<br>Refinancing</li><li>The Ultimate Guide to<br>Renovation Loans</li><li>Make a Payment</li><li>File a Complaint</li></ul>
  </div>
  <div class="abs fcol" style="left:991px">
    <h4>More Resources</h4>
    <ul><li>Beacon Gives</li><li>Careers</li><li>Today's Rates</li></ul>
    <h4 class="inline">Contact</h4>
    <ul><li>Branch Locations</li><li>Find a Mortgage Loan<br>Originator</li></ul>
  </div>

  <div class="abs legal"><span>Copyright © 2026. All Rights Reserved</span><span>Privacy Policy | Terms and Conditions</span></div>
</div>
</body>
</html>
```